Pelvane Tonic Social Media Graphics

Focusing on the Pelvane Tonic product, create 6-7 individual social media graphics (square size). For the color scheme of the graphics, they should all be complementary with the Pelvane Tonic bottle colors.

Note: each graphic should have one of the 3 pictures of the bottle on it and/or one of the images with a person on it (several pics attached)/only use stock photography that I provided.

Target Market(s)

men and women who need to lose weight

Industry/Entity Type

health and wellness

Colors
A7469A
B969AE
D3A5CF
EDDBEB
F8F0F9

Requirements
Must have
• product pictures
Nice to have
• stock photography that is included

```html
<!DOCTYPE html>
<html lang="en">
<head>
<meta charset="utf-8">
<title>Pelvane Tonic Social Media Graphics</title>
<link href="https://fonts.googleapis.com/css2?family=Catamaran:wght@300;400;700&display=swap" rel="stylesheet">
<style>
:root{
  --stage:#a3a3a3;
  --plum-dark:#5b2c57;
  --plum:#a7469a;
  --orchid:#b969ae;
  --lilac:#d3a5cf;
  --blush:#eddbeb;
  --mist:#f8f0f9;
  --ink:#3a2338;
  --white:#ffffff;
}
*{box-sizing:border-box;margin:0;padding:0}
html,body{width:1200px;height:1140px;overflow:hidden}
body{background:var(--stage);font-family:"Catamaran",sans-serif;color:var(--plum-dark);position:relative}
.tile{position:absolute;width:285px;height:285px;background:var(--white);overflow:hidden}
.tile-1{left:141px;top:100px}.tile-2{left:455px;top:100px}.tile-3{left:774px;top:100px}
.tile-4{left:141px;top:427px}.tile-5{left:455px;top:427px}.tile-6{left:774px;top:427px}
.tile-7{left:141px;top:754px}
.abs{position:absolute}
.headline{position:absolute;font-size:15px;line-height:18px;font-weight:300;color:var(--plum-dark);white-space:nowrap;z-index:3}
.headline b{font-weight:700}
.headline .accent{color:var(--plum)}
.photo{position:absolute;background:linear-gradient(160deg,#f4ece9 0%,#d8b5a0 55%,#a97a60 100%)}
.photo.soft{background:linear-gradient(160deg,#ffffff 0%,#efe3df 50%,#c79c84 100%)}
.bottle{position:absolute;border-radius:10px 10px 6px 6px;background:linear-gradient(180deg,#fafafa 0%,#f1f1f3 45%,var(--lilac) 78%,var(--orchid) 100%);box-shadow:0 2px 4px rgba(0,0,0,.15)}
.bottle-group{position:absolute;display:flex;gap:2px}
.bottle-group .bottle{position:relative;flex:1;height:100%}
.wave{position:absolute;left:0;width:285px;z-index:2}
.wave.bottom{bottom:0}
.wave.top{top:0}
.checklist{position:absolute;list-style:none;font-size:6px;line-height:14px;color:var(--ink);z-index:3}
.checklist li{display:flex;align-items:center;gap:5px}
.checklist svg{width:7px;height:7px}
.benefits{position:absolute;list-style:none;font-size:5.6px;line-height:6.5px;color:var(--ink);z-index:3}
.benefits li{display:flex;align-items:center;gap:5px;position:absolute;white-space:nowrap}
.icon{width:15px;height:15px;border-radius:50%;background:var(--plum);display:flex;align-items:center;justify-content:center;flex:none}
.icon svg{width:8px;height:8px}
.ring{position:absolute;border-radius:50%;border:1px solid var(--orchid)}
.round-photo{position:absolute;border-radius:50%;overflow:hidden}
.blob{position:absolute;border-radius:50%;background:linear-gradient(160deg,var(--mist),var(--blush))}
.tile-7 .headline{right:19px;top:34px;text-align:right;font-size:21px;line-height:24px}
</style>
</head>
<body>

<svg width="0" height="0" style="position:absolute">
  <defs>
    <linearGradient id="pink-band" x1="0" y1="0" x2="1" y2="0">
      <stop offset="0" stop-color="#f6c6e6"/>
      <stop offset="0.6" stop-color="#f5a9d9"/>
      <stop offset="1" stop-color="#f07cc8"/>
    </linearGradient>
    <symbol id="tick" viewBox="0 0 10 10"><path d="M1.5 5.2l2.3 2.4 4.7-5.6" fill="none" stroke="currentColor" stroke-width="1.6" stroke-linecap="round" stroke-linejoin="round"/></symbol>
    <symbol id="wave-bottom" viewBox="0 0 285 55"><path d="M0 28 C60 48 140 40 285 2 L285 55 L0 55Z" fill="url(#pink-band)"/><path d="M0 22 C60 42 140 34 285 -4" fill="none" stroke="#f3a3d6" stroke-width="1.4"/></symbol>
    <symbol id="wave-top" viewBox="0 0 285 55"><path d="M0 0 L285 0 L285 40 C220 50 170 52 110 30 C70 16 30 18 0 28Z" fill="url(#pink-band)"/><path d="M0 34 C30 24 70 22 110 36 C170 58 220 56 285 46" fill="none" stroke="#f3a3d6" stroke-width="1.4"/></symbol>
  </defs>
</svg>

<!-- Graphic 1 -->
<section class="tile tile-1">
  <div class="photo soft" role="img" aria-label="Woman in white sportswear measuring her waist with a tape measure" style="left:150px;top:0;width:135px;height:250px"></div>
  <h2 class="headline" style="left:15px;top:20px">Burn Fat Faster<br><b>Discover the <span class="accent">Simple Detox</span></b><br>Your Body Needs!</h2>
  <div class="bottle" role="img" aria-label="Pelvane Tonic supplement bottle" style="left:16px;top:82px;width:58px;height:98px"></div>
  <ul class="checklist" style="left:18px;top:196px">
    <li><svg style="color:var(--plum)"><use href="#tick"/></svg>Melt away stubborn fat, especially belly &amp; back fat</li>
    <li><svg style="color:var(--plum)"><use href="#tick"/></svg>Accelerate overall weight loss</li>
    <li><svg style="color:var(--plum)"><use href="#tick"/></svg>Boost energy and mental clarity</li>
    <li><svg style="color:var(--plum)"><use href="#tick"/></svg>Get whiter eyes and glowing skin</li>
  </ul>
  <svg class="wave bottom" height="55"><use href="#wave-bottom"/></svg>
</section>

<!-- Graphic 2 -->
<section class="tile tile-2">
  <h2 class="headline" style="left:19px;top:22px">Struggling to <span class="accent">Lose Weight?</span><br><b>Try This <span class="accent">Fat Flush Secret</span></b></h2>
  <div class="photo soft" role="img" aria-label="Smiling woman in sports top holding a bathroom scale" style="left:125px;top:20px;width:160px;height:225px"></div>
  <div class="bottle-group" role="img" aria-label="Three Pelvane Tonic bottles" style="left:19px;top:78px;width:100px;height:66px"><div class="bottle"></div><div class="bottle"></div><div class="bottle"></div></div>
  <ul class="benefits" style="left:17px;top:176px">
    <li style="top:0"><span class="icon"><svg style="color:#fff"><use href="#tick"/></svg></span>Melt away stubborn fat,<br>especially belly &amp; back fat</li>
    <li style="top:19px"><span class="icon"><svg style="color:#fff"><use href="#tick"/></svg></span>Accelerate overall weight loss</li>
    <li style="top:39px"><span class="icon"><svg style="color:#fff"><use href="#tick"/></svg></span>Boost energy and mental clarity</li>
    <li style="top:58px"><span class="icon"><svg style="color:#fff"><use href="#tick"/></svg></span>Get whiter eyes and glowing skin</li>
  </ul>
  <svg class="wave bottom" height="55"><use href="#wave-bottom"/></svg>
</section>

<!-- Graphic 3 -->
<section class="tile tile-3">
  <div class="photo soft" role="img" aria-label="Smiling woman holding an apple and a bathroom scale" style="left:0;top:8px;width:112px;height:247px"></div>
  <h2 class="headline" style="left:115px;top:18px"><b>Detox and Burn Fat</b><br><span class="accent">The 1-Step Solution for</span><br>a Slimmer You</h2>
  <div class="bottle-group" role="img" aria-label="Three Pelvane Tonic bottles" style="left:124px;top:90px;width:98px;height:66px"><div class="bottle"></div><div class="bottle"></div><div class="bottle"></div></div>
  <ul class="benefits" style="left:106px;top:181px">
    <li style="left:0;top:0"><span class="icon"><svg style="color:#fff"><use href="#tick"/></svg></span>Melt away stubborn fat,<br>especially belly &amp; back fat</li>
    <li style="left:0;top:21px"><span class="icon"><svg style="color:#fff"><use href="#tick"/></svg></span>Accelerate<br>overall weight loss</li>
    <li style="left:98px;top:0"><span class="icon"><svg style="color:#fff"><use href="#tick"/></svg></span>Boost energy<br>and mental clarity</li>
    <li style="left:98px;top:21px"><span class="icon"><svg style="color:#fff"><use href="#tick"/></svg></span>Get whiter eyes<br>and glowing skin</li>
  </ul>
  <svg class="wave bottom" height="55"><use href="#wave-bottom"/></svg>
</section>

<!-- Graphic 4 -->
<section class="tile tile-4">
  <h2 class="headline" style="left:15px;top:20px">Accelerate <span class="accent">Your Weight Loss</span><br><b>With This Easy <span class="accent">Fat Flush</span></b></h2>
  <div class="bottle" role="img" aria-label="Pelvane Tonic supplement bottle" style="left:23px;top:76px;width:55px;height:97px"></div>
  <div class="ring" style="left:127px;top:54px;width:156px;height:156px"></div>
  <div class="round-photo photo" role="img" aria-label="Fit woman in black sportswear measuring her waist" style="left:133px;top:60px;width:144px;height:144px;background:linear-gradient(160deg,#dfe2e8,#b88e74 60%,#6f4a38)"></div>
  <ul class="checklist" style="left:18px;top:196px">
    <li><svg style="color:var(--plum)"><use href="#tick"/></svg>Melt away stubborn fat, especially belly &amp; back fat</li>
    <li><svg style="color:var(--plum)"><use href="#tick"/></svg>Accelerate overall weight loss</li>
    <li><svg style="color:var(--plum)"><use href="#tick"/></svg>Boost energy and mental clarity</li>
    <li><svg style="color:var(--plum)"><use href="#tick"/></svg>Get whiter eyes and glowing skin</li>
  </ul>
  <svg class="wave bottom" height="55"><use href="#wave-bottom"/></svg>
</section>

<!-- Graphic 5 -->
<section class="tile tile-5">
  <div class="abs" style="left:0;top:30px;width:285px;height:214px;background:linear-gradient(180deg,#ffffff,#f4f2f4 60%,#ecebed)"></div>
  <svg class="wave top" height="55"><use href="#wave-top"/></svg>
  <h2 class="headline" style="left:15px;top:32px"><b>Cleanse <span class="accent">Your Liver</span></b><br><span class="accent">Burn Fat Faster</span><br>The Ultimate Solution</h2>
  <div class="bottle" role="img" aria-label="Pelvane Tonic supplement bottle lying tilted" style="left:30px;top:106px;width:72px;height:116px;transform:rotate(-12deg)"></div>
  <div class="ring" style="left:127px;top:80px;width:156px;height:156px"></div>
  <div class="round-photo photo soft" role="img" aria-label="Woman in white sports top with hands on her waist" style="left:133px;top:86px;width:144px;height:144px"></div>
  <ul class="benefits" style="left:17px;top:251px">
    <li style="left:0;top:0"><span class="icon"><svg style="color:#fff"><use href="#tick"/></svg></span>Melt away stubborn fat,<br>especially belly &amp; back fat</li>
    <li style="left:99px;top:0"><span class="icon"><svg style="color:#fff"><use href="#tick"/></svg></span>Boost energy<br>and mental clarity</li>
    <li style="left:179px;top:0"><span class="icon"><svg style="color:#fff"><use href="#tick"/></svg></span>Accelerate<br>overall weight loss</li>
  </ul>
</section>

<!-- Graphic 6 -->
<section class="tile tile-6">
  <div class="photo soft" role="img" aria-label="Woman in white sportswear measuring her waist with a tape measure" style="left:0;top:0;width:195px;height:260px"></div>
  <div class="blob" style="left:204px;top:74px;width:140px;height:140px"></div>
  <h2 class="headline" style="left:117px;top:26px"><b>Flush Away</b><br><b>5-10 Pounds <span class="accent">of Toxic Fat</span></b><br>in Just Weeks!</h2>
  <div class="bottle" role="img" aria-label="Pelvane Tonic supplement bottle" style="left:213px;top:95px;width:55px;height:97px"></div>
  <ul class="benefits" style="left:113px;top:183px">
    <li style="top:0"><span class="icon"><svg style="color:#fff"><use href="#tick"/></svg></span>Melt away stubborn fat,<br>especially belly &amp; back fat</li>
    <li style="top:19px"><span class="icon"><svg style="color:#fff"><use href="#tick"/></svg></span>Accelerate overall weight loss</li>
    <li style="top:38px"><span class="icon"><svg style="color:#fff"><use href="#tick"/></svg></span>Boost energy and mental clarity</li>
  </ul>
  <svg class="wave bottom" height="55"><use href="#wave-bottom"/></svg>
</section>

<!-- Graphic 7 -->
<section class="tile tile-7">
  <svg class="wave top" height="55"><use href="#wave-top"/></svg>
  <div class="blob" style="left:188px;top:160px;width:240px;height:240px"></div>
  <h2 class="headline"><span>The Hidden Key</span><br><span class="accent" style="color:var(--plum-dark);font-weight:300">to Weight Loss</span><br><b>Liver Health</b></h2>
  <div class="photo soft" role="img" aria-label="Smiling woman flexing her arm and holding a bathroom scale" style="left:0;top:72px;width:190px;height:213px"></div>
  <div class="bottle-group" role="img" aria-label="Three Pelvane Tonic bottles" style="left:166px;top:190px;width:99px;height:66px"><div class="bottle"></div><div class="bottle"></div><div class="bottle"></div></div>
</section>

</body>
</html>
```